New Personal Trainer needs poster to attract clients

Hi I am a personal trainer working inside a busy gym. My sole base of clients is from the gym itself where I compete with other trainers for business.
New company so my brand is still not noticed by the public.
My company name is Stridewell PT.
I am looking for a poster that will attract attention and increase awareness of my brand. My market will be mostly overweight men/women aged from 25-55 years old.
I would like pics of some sort on there that would be appropriate for my target market. Design needs to be colorful to attract attention.

My name and number must be added as well as facebook details
Dean Harlow
0427390518
(Facebook Symbol) Dean Harlow PT

Target Market(s)

Overweight men and women aged 25-55 years. Some would be mothers with young children

Industry/Entity Type

Fitness

Font styles to use
Sans Serif

Requirements
Must have
• My Logo.
• Pictures.
• Bright Attractive colours
• My name and number
• Slogan
Nice to have
• Slogan I'm leaning towards is "Building a Better You" but open to any ideas with this.

```html
<!DOCTYPE html>
<html lang="en">
<head>
<meta charset="utf-8">
<title>Stridewell PT – Dean Harlow Personal Trainer Poster</title>
<link rel="stylesheet" href="https://fonts.googleapis.com/css2?family=Arimo:wght@400&family=Montserrat:wght@500&family=Roboto+Condensed:wght@400;700&display=swap">
<style>
  :root {
    --navy: #0e1e2e;
    --navy-deep: #08121c;
    --band-dark: #1a2430;
    --blue: #1c8fe0;
    --blue-bright: #2aa3f0;
    --yellow: #ffd500;
    --orange: #f39a1e;
    --social-blue: #3b5a9a;
    --ink: #111111;
    --white: #ffffff;
  }
  html, body {
    margin: 0;
    padding: 0;
    width: 1000px;
    height: 1200px;
    overflow: hidden;
    background: var(--white);
  }
  .poster {
    position: relative;
    width: 1000px;
    height: 1200px;
  }
  .poster__art {
    position: absolute;
    inset: 0;
  }
  .brand-name {
    position: absolute;
    left: 560px;
    top: 130px;
    width: 296px;
    text-align: right;
    font-family: "Roboto Condensed", sans-serif;
    font-weight: 700;
    font-size: 42px;
    line-height: 1;
    color: var(--yellow);
    letter-spacing: 1px;
  }
  .trainer-name {
    position: absolute;
    right: 143px;
    top: 212px;
    margin: 0;
    text-align: right;
    font-family: "Montserrat", sans-serif;
    font-weight: 500;
    font-size: 60px;
    line-height: 58px;
    color: var(--white);
  }
  .trainer-role {
    position: absolute;
    right: 135px;
    top: 338px;
    font-family: "Montserrat", sans-serif;
    font-weight: 500;
    font-size: 21px;
    letter-spacing: 3.2px;
    color: var(--white);
  }
  .slogan {
    position: absolute;
    left: 568px;
    width: 296px;
    top: 400px;
    margin: 0;
    text-align: center;
    font-family: "Roboto Condensed", sans-serif;
    font-weight: 700;
    font-size: 64px;
    line-height: 62px;
    color: var(--ink);
    text-transform: uppercase;
  }
  .prompt {
    position: absolute;
    right: 155px;
    top: 598px;
    margin: 0;
    text-align: right;
    font-family: "Arimo", sans-serif;
    font-size: 31px;
    line-height: 34px;
    letter-spacing: 0.4px;
    color: var(--ink);
  }
  .cta {
    position: absolute;
    left: 553px;
    top: 686px;
    width: 340px;
    height: 86px;
    border-radius: 32px 0 0 32px;
    background: var(--yellow);
    display: flex;
    align-items: center;
    justify-content: center;
    text-align: center;
    font-family: "Roboto Condensed", sans-serif;
    font-weight: 700;
    font-size: 32px;
    line-height: 33px;
    color: var(--ink);
  }
  .contact {
    position: absolute;
    left: 528px;
    display: flex;
    align-items: center;
    gap: 20px;
    font-family: "Roboto Condensed", sans-serif;
    font-weight: 400;
    color: var(--ink);
  }
  .contact--phone { top: 792px; font-size: 48px; letter-spacing: 1.5px; }
  .contact--social { top: 854px; font-size: 43px; }
  .contact__icon { width: 40px; height: 40px; flex: none; }
</style>
</head>
<body>
<main class="poster">
  <svg class="poster__art" width="1000" height="1200" viewBox="0 0 1000 1200">
    <defs>
      <linearGradient id="gymGrad" x1="0" y1="0" x2="0" y2="1">
        <stop offset="0" stop-color="#f1f4f6"/>
        <stop offset="0.45" stop-color="#d5dadf"/>
        <stop offset="0.65" stop-color="#9fa4aa"/>
        <stop offset="0.8" stop-color="#e58770"/>
        <stop offset="1" stop-color="#e06a52"/>
      </linearGradient>
      <linearGradient id="athleteGrad" x1="0" y1="0" x2="1" y2="1">
        <stop offset="0" stop-color="#0f1b28"/>
        <stop offset="0.35" stop-color="#5a3a28"/>
        <stop offset="0.55" stop-color="#8a5a3c"/>
        <stop offset="0.8" stop-color="#3a2a22"/>
        <stop offset="1" stop-color="#0f1b28"/>
      </linearGradient>
      <linearGradient id="womanGrad" x1="0" y1="0" x2="1" y2="1">
        <stop offset="0" stop-color="#111c28"/>
        <stop offset="0.45" stop-color="#a4725a"/>
        <stop offset="0.7" stop-color="#1a1a1e"/>
        <stop offset="1" stop-color="#111c28"/>
      </linearGradient>
      <linearGradient id="benchGrad" x1="0" y1="0" x2="1" y2="1">
        <stop offset="0" stop-color="#6c6f74"/>
        <stop offset="0.45" stop-color="#a87458"/>
        <stop offset="0.75" stop-color="#2d55a0"/>
        <stop offset="1" stop-color="#3c3f45"/>
      </linearGradient>
      <linearGradient id="torsoGrad" x1="0" y1="0" x2="0" y2="1">
        <stop offset="0" stop-color="#ffffff"/>
        <stop offset="0.25" stop-color="#f4ded4"/>
        <stop offset="0.6" stop-color="#d89a82"/>
        <stop offset="0.8" stop-color="#2a2a2a"/>
        <stop offset="1" stop-color="#161616"/>
      </linearGradient>
    </defs>

    <g role="img" aria-label="Photo: woman training with a kettlebell beside a trainer in a bright gym">
      <rect class="photo photo--gym" x="120" y="97" width="320" height="253" fill="url(#gymGrad)"/>
    </g>

    <polygon class="header-chevron header-chevron--outer" points="410,97 455,97 400,235 455,372 410,372 358,235" fill="var(--blue)"/>
    <polygon class="header-panel" points="455,97 893,97 893,372 455,372 400,235" fill="var(--navy)"/>
    <polygon class="header-chevron header-chevron--inner" points="470,120 500,120 445,235 500,350 470,350 415,235" fill="var(--blue-bright)"/>
    <line class="brand-rule" x1="575" y1="184" x2="856" y2="184" stroke="var(--blue)" stroke-width="2"/>

    <rect class="accent-band" x="120" y="350" width="335" height="14" fill="var(--yellow)"/>
    <rect class="accent-band" x="440" y="372" width="453" height="16" fill="var(--yellow)"/>

    <polygon class="edge-band edge-band--dark" points="415,372 440,388 525,612 420,862 392,850 498,612" fill="var(--band-dark)"/>
    <polygon class="edge-band edge-band--blue" points="120,365 420,365 510,612 400,850 380,846 490,612 405,377 120,377" fill="var(--blue)"/>
    <g role="img" aria-label="Photo: muscular man posing against a dark studio background">
      <polygon class="photo photo--athlete" points="120,377 405,377 490,612 380,846 120,782" fill="url(#athleteGrad)"/>
    </g>

    <g role="img" aria-label="Photo: smiling woman holding small yellow dumbbells">
      <polygon class="photo photo--woman" points="120,790 376,855 326,1130 120,1130" fill="url(#womanGrad)"/>
    </g>

    <polygon class="edge-band edge-band--dark" points="458,845 690,985 690,1010 455,862" fill="var(--band-dark)"/>
    <polygon class="edge-band edge-band--blue" points="384,856 455,862 690,1010 690,1130 680,1130 680,1018 452,874 392,868 342,1130 334,1130" fill="var(--blue)"/>
    <g role="img" aria-label="Photo: man doing a one-arm dumbbell row on a gym bench">
      <polygon class="photo photo--bench" points="392,868 452,874 680,1018 680,1130 342,1130" fill="url(#benchGrad)"/>
    </g>

    <g role="img" aria-label="Photo: woman's toned midsection holding two dumbbells">
      <rect class="photo photo--torso" x="690" y="925" width="203" height="205" fill="url(#torsoGrad)"/>
    </g>
  </svg>

  <div class="brand-name">STRIDEWELL PT</div>
  <h1 class="trainer-name">DEAN<br>HARLOW</h1>
  <div class="trainer-role">PERSONAL TRAINER</div>

  <h2 class="slogan">Building<br>a better<br>you!</h2>
  <p class="prompt">Ready to make<br>the commitment?</p>
  <div class="cta">CONTACT DEAN<br>TODAY!</div>

  <div class="contact contact--phone">
    <svg class="contact__icon" viewBox="0 0 40 40" aria-hidden="true">
      <circle cx="20" cy="20" r="19" fill="var(--orange)"/>
      <path d="M14 11c1-1 2.5-1 3 .3l1.6 3.6c.4 1-.1 1.8-.9 2.3l-1 .7c1 2.4 2.8 4.3 5.3 5.4l.7-1c.6-.8 1.4-1.2 2.3-.8l3.6 1.6c1.2.5 1.3 2 .3 3l-1.5 1.5c-1.3 1.3-3.4 1.5-5.3.6-4.7-2.1-8.3-5.7-10.4-10.4-.9-1.9-.7-4 .6-5.3z" fill="var(--white)"/>
    </svg>
    <span>0427390518</span>
  </div>
  <div class="contact contact--social">
    <svg class="contact__icon" viewBox="0 0 40 40" aria-hidden="true">
      <circle cx="20" cy="20" r="19" fill="var(--social-blue)"/>
    </svg>
    <span>Dean Harlow PT</span>
  </div>
</main>
</body>
</html>
```